Ridgeline Outfitters Business Cards

Recently had a logo done with Artfolio and now looking for a business card to go along with it.

Target Market(s)

Ridgeline Outfitters is a weapons dealer. My market will be primarily men, hunting, shooting type.

Industry/Entity Type

Business

Contact Information for Business Card

I selected double sided, but this is not required, single or double is going to be fine. I picture the logo on one side, or perhaps just the circle which contains "RO" with the remaining info on the other side.

Font styles to use
Sans Serif

Requirements
Must have
• My name: Milo Brandt
• Title: Owner
• tel: 612-555-0187
• web: www.ridgelineoutfittersmn.example
Nice to have
• I like the concept of a black business card. I would like to keep the colors monotone, black, grey, white or red. Red is acceptable because it is in the logo. I have also seen cards that are matte black with shiny black as well, perhaps for the logo (or circle RO) part of the logo.
• I will upload a couple of the logos for use, and also an example I just found of the black on black. and some others that have a nice contrast.
Should not have
• lots of colors are not wanted.

```html
<!DOCTYPE html>
<html lang="en">
<head>
<meta charset="utf-8">
<title>Ridgeline Outfitters Business Cards</title>
<link rel="stylesheet" href="https://fonts.googleapis.com/css2?family=Montserrat:wght@500;600;700&display=swap">
<style>
  :root {
    --canvas: #e9e7e4;
    --card-black: #050505;
    --card-red: #ec1c24;
    --card-grey: #5f5f5f;
    --ring-grey: #6a6a6a;
    --ink-white: #ffffff;
    --ink-black: #0a0a0a;
  }
  * { margin: 0; padding: 0; box-sizing: border-box; }
  html, body {
    width: 1200px; height: 866px; overflow: hidden;
    background: var(--canvas);
    font-family: "Montserrat", sans-serif;
  }
  .sheet {
    width: 1200px; height: 866px;
    display: flex; flex-direction: column;
    align-items: center; justify-content: center; gap: 56px;
  }
  .card {
    position: relative;
    width: 560px; height: 320px;
    background: var(--card-black);
    overflow: hidden;
    box-shadow: 0 10px 24px rgba(0,0,0,0.25);
  }
  .card-shapes { position: absolute; inset: 0; }
  .shape-red { fill: var(--card-red); }
  .shape-grey { fill: var(--card-grey); }

  /* Front */
  .brand {
    position: absolute; left: 44px; top: 108px;
    display: flex; align-items: center; gap: 14px;
  }
  .brand-ring {
    width: 62px; height: 62px; border-radius: 50%;
    border: 5px solid var(--ring-grey);
  }
  .brand-name {
    color: var(--card-red);
    font-weight: 700; font-size: 21px;
    letter-spacing: 1.5px; text-transform: uppercase;
  }

  /* Back */
  .holder { position: absolute; left: 30px; top: 66px; }
  .holder-name {
    color: var(--ink-white); font-weight: 600; font-size: 25px;
  }
  .holder-title {
    color: var(--ink-black); font-weight: 600; font-size: 14px; margin-top: 2px;
  }
  .monogram {
    position: absolute; left: 398px; top: 28px;
    width: 84px; height: 84px; border-radius: 50%;
    border: 5px solid var(--ring-grey);
    display: flex; align-items: center; justify-content: center;
    color: var(--card-red); font-weight: 700; font-size: 28px; letter-spacing: 1px;
  }
  .contact-list { position: absolute; right: 14px; top: 140px; list-style: none; }
  .contact-pill {
    display: flex; align-items: center; gap: 12px;
    height: 28px; border-radius: 14px;
    background: var(--card-red);
    padding: 0 14px 0 12px;
    color: var(--ink-white); font-weight: 600;
    margin-bottom: 16px;
  }
  .contact-pill.phone { width: 230px; margin-left: auto; font-size: 15px; letter-spacing: 0.5px; }
  .contact-pill.web { width: 266px; font-size: 11.5px; }
  .contact-icon { width: 16px; height: 16px; flex: none; }
  .contact-text { flex: 1; text-align: center; white-space: nowrap; }
</style>
</head>
<body>
<main class="sheet">

  <section class="card card-front" aria-label="Business card front">
    <svg class="card-shapes" viewBox="0 0 560 320" width="560" height="320" aria-hidden="true">
      <polygon class="shape-grey" points="330,0 560,0 560,45 475,123"/>
      <polygon class="shape-red" points="260,320 560,45 560,320"/>
    </svg>
    <div class="brand">
      <span class="brand-ring"></span>
      <span class="brand-name">Ridgeline Outfitters</span>
    </div>
  </section>

  <section class="card card-back" aria-label="Business card back">
    <svg class="card-shapes" viewBox="0 0 560 320" width="560" height="320" aria-hidden="true">
      <polygon class="shape-red" points="0,0 345,0 25,320 0,320"/>
      <polygon class="shape-grey" points="185,153 352,320 25,320"/>
    </svg>
    <div class="holder">
      <p class="holder-name">Milo Brandt</p>
      <p class="holder-title">Owner</p>
    </div>
    <div class="monogram">RO</div>
    <ul class="contact-list">
      <li class="contact-pill phone">
        <svg class="contact-icon" viewBox="0 0 24 24" aria-hidden="true">
          <path fill="#fff" d="M6.6 10.8a15.1 15.1 0 0 0 6.6 6.6l2.2-2.2c.3-.3.7-.4 1-.2 1.1.4 2.3.6 3.6.6.6 0 1 .4 1 1V20c0 .6-.4 1-1 1A17 17 0 0 1 3 4c0-.6.4-1 1-1h3.5c.6 0 1 .4 1 1 0 1.3.2 2.5.6 3.6.1.3 0 .7-.2 1z"/>
        </svg>
        <span class="contact-text">612 - 555 - 0187</span>
      </li>
      <li class="contact-pill web">
        <svg class="contact-icon" viewBox="0 0 24 24" aria-hidden="true">
          <circle cx="12" cy="12" r="10" fill="#fff"/>
          <path fill="#ec1c24" d="M8 6c2 0 3 1 3 2.5S9.5 11 8 11 6 12.5 7 14s-1 3-2.5 1.5A8 8 0 0 1 8 6zm7 8c1.5 0 3 1 2.5 2.5S15 19 14 18s-.5-4 1-4z"/>
        </svg>
        <span class="contact-text">www.ridgelineoutfittersmn.example</span>
      </li>
    </ul>
  </section>

</main>
</body>
</html>
```